Sports Therapy and Personal Training

I need a business card design for a new business based in Toronto called "Holbrin Athletics" I am a sports therapist as well as a strength and conditioning coach, therefore I work mainly with high level athletes and physically active people. I am starting my own therapy/training business. The services I will be offering include fitness consultation, personal training, athlete assessments, and rehabilitation therapy. These services will be delivered in peoples homes and/or a facility in which I rent space.

The final design should communicate "high-end" and "quality"

Target Market(s)

athletes and physically active people

Industry/Entity Type

Fitness

Requirements
Must have
• 1. The business logo - files attached

2. my name and credentials

Derek Falloway - CAT(C), CK, CSCS,

Certified Athletic Therapist
Strength and Conditioning Specialist

3. website - www.holbrinathletics.example

4. email address - derek@holbrinathletics.example

5. phone number

```html
<!DOCTYPE html>
<html lang="en">
<head>
<meta charset="utf-8">
<title>Holbrin Athletics – Business Card</title>
<link href="https://fonts.googleapis.com/css2?family=Arimo:wght@400;700&display=swap" rel="stylesheet">
<style>
  :root {
    --backdrop: #e4e4e4;
    --card-white: #ffffff;
    --card-grey: #9d9da0;
    --ink-dark: #3a3a3c;
    --ink-mid: #555558;
    --ink-soft: #8a8a8d;
    --accent-red: #d8262d;
    --faint-grey: #efefef;
    --pattern-tone: #a7a7aa;
  }
  html, body {
    margin: 0;
    padding: 0;
    width: 1200px;
    height: 900px;
    overflow: hidden;
    background: var(--backdrop);
    font-family: "Arimo", Arial, sans-serif;
  }
  .stage { position: relative; width: 1200px; height: 900px; }

  .card {
    position: absolute;
    left: 232px;
    width: 736px;
    overflow: hidden;
    box-shadow: 0 2px 6px rgba(0,0,0,0.18);
  }
  .card--front { top: 20px; height: 444px; background: var(--card-white); }
  .card--back  { top: 468px; height: 416px; background: var(--card-grey); }

  .brand__mark { position: absolute; width: 118px; height: 118px; }
  .brand__name {
    position: absolute;
    margin: 0;
    font-weight: 700;
    font-size: 48px;
    letter-spacing: 3px;
    line-height: 1;
    white-space: nowrap;
  }
  .brand__tagline {
    position: absolute;
    font-weight: 700;
    font-size: 14px;
    letter-spacing: 2.2px;
    text-transform: uppercase;
    white-space: nowrap;
  }

  .card--front .brand__mark { left: 30px; top: 34px; background: var(--ink-mid); }
  .card--front .brand__name { left: 168px; top: 56px; color: var(--ink-dark); }
  .card--front .brand__tagline { left: 170px; top: 112px; color: var(--ink-soft); }

  .front-decor {
    position: absolute;
    left: 440px; top: 150px;
    width: 296px; height: 294px;
    background: var(--faint-grey);
  }

  .person { position: absolute; left: 30px; top: 180px; }
  .person__name {
    margin: 0 0 12px;
    font-size: 36px;
    font-weight: 700;
    line-height: 40px;
    color: var(--ink-dark);
  }
  .person__title {
    margin: 0;
    font-size: 21px;
    line-height: 25px;
    color: var(--ink-mid);
  }

  .contact {
    position: absolute; left: 30px; top: 300px;
    margin: 0; padding: 0; list-style: none;
    font-size: 20px; line-height: 30px; color: var(--ink-mid);
  }
  .contact__label { color: var(--accent-red); }

  .back-pattern {
    position: absolute; inset: 0;
    background: radial-gradient(circle at 50% 50%, var(--card-grey) 0%, var(--pattern-tone) 100%);
  }
  .card--back .brand__mark { left: 34px; top: 140px; background: var(--card-white); }
  .card--back .brand__name { left: 172px; top: 172px; color: var(--card-white); }
  .card--back .brand__tagline { left: 174px; top: 228px; color: var(--card-white); }
</style>
</head>
<body>
<main class="stage">
  <section class="card card--front" aria-label="Business card front">
    <div class="front-decor" aria-hidden="true"></div>

    <span class="brand__mark" aria-hidden="true"></span>
    <p class="brand__name">Holbrin Athletics</p>
    <div class="brand__tagline">Sports Medicine • Strength and Conditioning</div>

    <div class="person">
      <h1 class="person__name">Derek Falloway</h1>
      <p class="person__title">Certified Athletic Therapist</p>
      <p class="person__title">Strength and Conditioning Specialist</p>
    </div>

    <ul class="contact">
      <li><span class="contact__label">p:</span> 416.555.0182</li>
      <li><span class="contact__label">e:</span> derek@holbrinathletics.example</li>
      <li><span class="contact__label">w:</span> www.holbrinathletics.example</li>
    </ul>
  </section>

  <section class="card card--back" aria-label="Business card back">
    <div class="back-pattern" role="img" aria-label="Faint repeating brand pattern across the card back"></div>
    <span class="brand__mark" aria-hidden="true"></span>
    <p class="brand__name">Holbrin Athletics</p>
    <div class="brand__tagline">Sports Medicine • Strength and Conditioning</div>
  </section>
</main>
</body>
</html>
```